Service business needs Business Card Design

Looking to create a new business card design that is both professional and unique the can highlight the many services we offer throughout the seasons. Our tagline is "The Steadfast Touch"
Licensed & Insured: PA392617 has to be small and on the back side of the card.
On the Front:
FirstName LastName
Title
We offer the following services:
Deck Repair and Maintenance
Deck Cleaning and Staining/Painting
Power Washing/House Washing
Landscape Lighting Installation
Christmas Lighting Installation

```html
<!DOCTYPE html>
<html lang="en">
<head>
<meta charset="utf-8">
<title>Clearway Services – Business Card</title>
<link href="https://fonts.googleapis.com/css2?family=Roboto:wght@400;500&display=swap" rel="stylesheet">
<style>
  :root {
    --brand-blue: #0d4f8b;
    --brand-blue-light: #1a63a8;
    --ink: #333333;
    --card-white: #ffffff;
    --card-back: #fcf8f8;
    --stage: #e8e5e0;
    --divider: #9a9a9a;
  }
  * { box-sizing: border-box; margin: 0; padding: 0; }
  html, body {
    width: 900px; height: 1200px; overflow: hidden;
    background: var(--stage);
    font-family: "Roboto", Arial, sans-serif;
  }
  .canvas { position: relative; width: 900px; height: 1200px; }

  .card {
    position: absolute;
    border-radius: 40px;
    overflow: hidden;
    box-shadow: 0 6px 18px rgba(0,0,0,0.18);
  }
  .card-front { left: 45px; top: 112px; width: 815px; height: 465px; background: var(--card-white); }
  .card-back  { left: 33px; top: 620px; width: 827px; height: 470px; background: var(--card-back); }

  /* front header */
  .brand-mark {
    position: absolute; left: 56px; top: 42px;
    display: flex; align-items: center; gap: 14px;
  }
  .brand-square { width: 36px; height: 36px; background: var(--brand-blue-light); }
  .brand-name {
    font-weight: 500; font-size: 30px; letter-spacing: 0.06em;
    color: var(--brand-blue-light); line-height: 1;
  }
  .owner { position: absolute; right: 45px; top: 46px; text-align: right; }
  .owner-name { font-size: 28px; color: var(--ink); line-height: 1.2; }
  .owner-title { font-size: 16px; color: var(--brand-blue); margin-top: 2px; }

  /* services band */
  .services-band {
    position: absolute; left: 0; top: 151px; width: 100%; height: 201px;
    background: var(--brand-blue);
  }
  .service { position: absolute; display: flex; align-items: center; gap: 10px; color: #fff; }
  .service-icon { width: 42px; height: 42px; flex: none; }
  .service-text { font-size: 20px; line-height: 25px; }
  .s-deck-repair   { left: 30px;  top: 34px; }
  .s-power-wash    { left: 265px; top: 30px; }
  .s-deck-clean    { left: 533px; top: 34px; }
  .s-christmas     { left: 108px; top: 110px; }
  .s-landscape     { left: 408px; top: 110px; }

  /* contact row */
  .contacts {
    position: absolute; left: 0; right: 0; top: 388px;
    display: flex; justify-content: center; align-items: center;
    font-size: 16px; color: var(--ink);
  }
  .contact { display: flex; align-items: center; gap: 7px; padding: 0 8px; }
  .contact-icon { width: 17px; height: 17px; flex: none; }
  .contact-icon.is-filled { fill: var(--brand-blue); }
  .contact-icon.is-outline { fill: none; stroke: var(--brand-blue); stroke-width: 2; }
  .contact-divider { width: 1px; height: 40px; background: var(--divider); }

  /* back */
  .back-circle {
    position: absolute; left: 338px; top: 60px; width: 150px; height: 150px;
    border-radius: 50%; background: var(--brand-blue-light);
  }
  .back-name {
    position: absolute; left: 0; right: 0; top: 240px; text-align: center;
    color: var(--brand-blue); font-weight: 500; line-height: 1;
  }
  .back-name-main { display: block; font-size: 80px; letter-spacing: 0.04em; }
  .back-name-sub { display: block; font-size: 34px; letter-spacing: 1.4em; margin-top: 12px; padding-left: 1.4em; }
  .tagline {
    position: absolute; left: 0; right: 0; top: 400px; text-align: center;
    font-size: 22px; letter-spacing: 0.85em; padding-left: 0.85em;
    color: var(--brand-blue); text-transform: uppercase;
  }
  .license {
    position: absolute; left: 0; right: 0; top: 442px; text-align: center;
    font-size: 12px; letter-spacing: 0.04em; color: var(--ink);
  }
</style>
</head>
<body>
<div class="canvas">

  <section class="card card-front">
    <div class="brand-mark">
      <span class="brand-square"></span>
      <span class="brand-name">CLEARWAY SERVICES</span>
    </div>
    <div class="owner">
      <p class="owner-name">Megan Colvard</p>
      <p class="owner-title">Owner and Founder</p>
    </div>

    <div class="services-band">
      <div class="service s-deck-repair">
        <svg class="service-icon" viewBox="0 0 42 42" fill="none" stroke="#fff" stroke-width="2.5">
          <path d="M3 38h36M6 38V30h8v-7h8v-7h8V9h8v29"/>
          <path d="M6 24 L34 4"/>
        </svg>
        <span class="service-text">Deck Repair<br>and Maintenance</span>
      </div>
      <div class="service s-power-wash">
        <svg class="service-icon" viewBox="0 0 42 42" fill="none" stroke="#fff" stroke-width="2.5">
          <path d="M4 4 L22 24"/>
          <path d="M22 24 l6 -4 l4 6 l-6 12 h-6 z" fill="#fff"/>
        </svg>
        <span class="service-text">Power Washing<br>and House Washing</span>
      </div>
      <div class="service s-deck-clean">
        <svg class="service-icon" viewBox="0 0 42 42" fill="#fff">
          <rect x="10" y="14" width="16" height="10" rx="3"/>
          <rect x="14" y="4" width="8" height="10"/>
          <path d="M15 24h6l-2 12h-3z"/>
          <path d="M30 15l8-3M30 19h9M30 23l8 3" stroke="#fff" stroke-width="2"/>
        </svg>
        <span class="service-text">Deck Cleaning<br>and Staining/Painting</span>
      </div>
      <div class="service s-christmas">
        <svg class="service-icon" viewBox="0 0 42 42" fill="none" stroke="#fff" stroke-width="2.5">
          <path d="M2 8 Q21 18 40 8"/>
          <ellipse cx="12" cy="26" rx="6" ry="9"/>
          <ellipse cx="30" cy="26" rx="6" ry="9"/>
        </svg>
        <span class="service-text">Christmas Lighting<br>and Installation</span>
      </div>
      <div class="service s-landscape">
        <svg class="service-icon" viewBox="0 0 42 42" fill="#fff">
          <path d="M21 2 l7 8 h-14z"/>
          <rect x="15" y="11" width="12" height="12"/>
          <rect x="19" y="23" width="4" height="13"/>
          <rect x="14" y="36" width="14" height="4"/>
        </svg>
        <span class="service-text">Landscape<br>and Lighting Installation</span>
      </div>
    </div>

    <div class="contacts">
      <span class="contact">
        <svg class="contact-icon is-filled" viewBox="0 0 24 24"><path d="M6.6 10.8a15 15 0 0 0 6.6 6.6l2.2-2.2a1 1 0 0 1 1-.25 11.4 11.4 0 0 0 3.6.57 1 1 0 0 1 1 1V20a1 1 0 0 1-1 1A17 17 0 0 1 3 4a1 1 0 0 1 1-1h3.5a1 1 0 0 1 1 1c0 1.25.2 2.45.57 3.57a1 1 0 0 1-.25 1z"/></svg>
        401-555-0147
      </span>
      <span class="contact-divider"></span>
      <span class="contact">
        <svg class="contact-icon is-outline" viewBox="0 0 24 24"><rect x="2" y="5" width="20" height="14"/><path d="M2 5l10 8 10-8"/></svg>
        info@clearwayservices
      </span>
      <span class="contact-divider"></span>
      <span class="contact">
        <svg class="contact-icon is-outline" viewBox="0 0 24 24"><circle cx="12" cy="12" r="10"/><path d="M2 12h20M12 2c3 3 3 17 0 20M12 2c-3 3-3 17 0 20"/></svg>
        https://clearwayservices.com
      </span>
    </div>
  </section>

  <section class="card card-back">
    <span class="back-circle"></span>
    <h1 class="back-name">
      <span class="back-name-main">CLEARWAY</span>
      <span class="back-name-sub">SERVICES</span>
    </h1>
    <p class="tagline">The Steadfast Touch</p>
    <p class="license">Licensed &amp; Insured: PA392617</p>
  </section>

</div>
</body>
</html>
```